Taomeng business card -we import and distributed Chinese herbal medicine into Australia for prac...

We need a business card for our recently purchased and rebranded company. We are a small family run business - husband and wife team. Our logo is red and black, and we would like the card to be white, with an element of gold in the design (the first cloud in the attached png) which when printed we would like embossed in gold. Our website uses Chinese water colour paintings in the banners (www.taomeng.net.au) so a design that is in harmony with this would be ideal.
side one needs to include:

Target Market(s)

potential customers

Industry/Entity Type

Health And Wellness

Contact Information for Business Card

Side 1
logo,
Edmund Varsk Director
Practitioner Support and Education
0491 722 413
edmund@taomeng.net.au
218 Colbury St, Brenlow, NR, 4190

side 2 needs to include:
logo
Priscilla Moult Director
Orders, Accounts and Despatch
0487 530 619
priscilla@taomeng.net.au

Font styles to use
Serif

Colors

Designer to choose colors to be used in the design.

Requirements
Must have
• black, red, gold colours
Nice to have
• we like the font papyrus (mac font)

```html
<!DOCTYPE html>
<html lang="en">
<head>
<meta charset="utf-8">
<title>Taomeng business cards</title>
<link href="https://fonts.googleapis.com/css2?family=Lato:wght@400;700&display=swap" rel="stylesheet">
<style>
  :root {
    --backdrop: #2a2a2c;
    --card: #fbfbfb;
    --ink: #1c2140;
    --text: #3a3a3a;
    --red: #e03a2a;
    --gold-light: #f3d77a;
    --gold-deep: #b8891f;
    --divider: #e2e2e2;
  }
  * { box-sizing: border-box; margin: 0; padding: 0; }
  html, body { width: 1200px; height: 900px; overflow: hidden; }
  body {
    background: var(--backdrop);
    font-family: "Lato", Arial, sans-serif;
    position: relative;
  }
  .card {
    position: absolute;
    width: 580px;
    height: 330px;
    background: var(--card);
    border-bottom: 9px solid var(--red);
    box-shadow: 0 14px 30px rgba(0,0,0,0.45);
    overflow: hidden;
  }
  .card--priscilla { left: 400px; top: 110px; }
  .card--edmund { left: 200px; top: 470px; }

  .brand {
    position: absolute;
    left: 36px;
    top: 100px;
    display: flex;
    align-items: center;
    gap: 14px;
  }
  .brand__seal {
    width: 34px;
    height: 64px;
    background: var(--red);
  }
  .brand__name {
    font-size: 42px;
    font-weight: 400;
    color: var(--ink);
    letter-spacing: 1px;
  }
  .divider {
    position: absolute;
    left: 284px;
    top: 70px;
    width: 1px;
    height: 160px;
    background: var(--divider);
  }
  .details {
    position: absolute;
    left: 302px;
    top: 84px;
    width: 260px;
    color: var(--text);
  }
  .details__name {
    font-size: 16px;
    font-weight: 700;
    color: var(--ink);
    text-transform: uppercase;
    letter-spacing: 0.3px;
    white-space: nowrap;
  }
  .details__title {
    color: var(--red);
    font-weight: 400;
  }
  .details__role { font-size: 14px; margin: 2px 0 6px; white-space: nowrap; }
  .details__line {
    display: flex;
    align-items: center;
    gap: 8px;
    font-size: 14px;
    line-height: 22px;
    white-space: nowrap;
  }
  .details__line svg { width: 12px; height: 12px; fill: var(--ink); flex: none; }
  .details__address { font-size: 14px; margin-top: 12px; white-space: nowrap; }
  .cloud {
    position: absolute;
    left: 180px;
    bottom: 4px;
    width: 120px;
    height: 46px;
    border-radius: 40px 40px 8px 8px;
    background: linear-gradient(135deg, var(--gold-light), var(--gold-deep));
  }
</style>
</head>
<body>

<section class="card card--priscilla">
  <div class="brand">
    <span class="brand__seal"></span>
    <span class="brand__name">Taomeng</span>
  </div>
  <div class="divider"></div>
  <div class="details">
    <p class="details__name">Priscilla Moult <span class="details__title">Director</span></p>
    <p class="details__role">Orders, Accounts and Despatch</p>
    <p class="details__line"><svg viewBox="0 0 12 12"><path d="M2 1h3l1 3-1.5 1a7 7 0 0 0 2.5 2.5L8 6l3 1v3a1 1 0 0 1-1 1A9 9 0 0 1 1 2a1 1 0 0 1 1-1z"/></svg>0487 530 619</p>
    <p class="details__line"><svg viewBox="0 0 12 12"><path d="M0 2h12v8H0z"/></svg>priscilla@taomeng.net.au</p>
    <p class="details__address">218 Colbury St, Brenlow, NR, 4190</p>
  </div>
  <div class="cloud" role="img" aria-label="Gold embossed auspicious cloud ornament"></div>
</section>

<section class="card card--edmund">
  <div class="brand">
    <span class="brand__seal"></span>
    <span class="brand__name">Taomeng</span>
  </div>
  <div class="divider"></div>
  <div class="details">
    <p class="details__name">Edmund Varsk <span class="details__title">Director</span></p>
    <p class="details__role">Practitioner support and Education</p>
    <p class="details__line"><svg viewBox="0 0 12 12"><path d="M2 1h3l1 3-1.5 1a7 7 0 0 0 2.5 2.5L8 6l3 1v3a1 1 0 0 1-1 1A9 9 0 0 1 1 2a1 1 0 0 1 1-1z"/></svg>0491 722 413</p>
    <p class="details__line"><svg viewBox="0 0 12 12"><path d="M0 2h12v8H0z"/></svg>edmund@taomeng.net.au</p>
    <p class="details__address">218 Colbury St, Brenlow, NR, 4190</p>
  </div>
  <div class="cloud" role="img" aria-label="Gold embossed auspicious cloud ornament"></div>
</section>

</body>
</html>
```